Buisness card

**Front Side:**

**[Your Company Logo]**
**Steadfast Upkeep Engineering**
*Keeping Your Equipment Running Smoothly*

**Contact Information:**
- **Name:** [dale Harwick
- **Title:** [owner
- **Phone:** [5073918246
- **Email:** dale@suevx.com

**Back Side:**

**Services Offered:**
- Routine Inspections
- Equipment Maintenance
- Emergency Repairs
- Consultation Services
- New installs
Tag line
Be proactive not reactive

```html
<!DOCTYPE html>
<html lang="en">
<head>
<meta charset="UTF-8">
<title>Steadfast Upkeep Engineering – Business Card</title>
<link rel="stylesheet" href="https://fonts.googleapis.com/css2?family=Poppins:wght@400;500;600;700;800;900&display=swap">
<style>
  :root {
    --bg: #2b2b2b;
    --navy: #0b2f7a;
    --deep-navy: #062a6e;
    --blue: #1a5fe0;
    --bright-blue: #1f7bff;
    --cyan: #12c6f5;
    --ink: #1b1b1b;
    --grey-ink: #4a4a4a;
    --card-white: #ffffff;
    --card-grey: #c9c9c9;
  }
  * { margin: 0; padding: 0; box-sizing: border-box; }
  html, body { width: 1200px; height: 800px; overflow: hidden; }
  body {
    background: var(--bg);
    font-family: "Poppins", sans-serif;
    display: flex;
    align-items: center;
    justify-content: center;
    gap: 40px;
  }
  .card {
    position: relative;
    width: 540px;
    height: 308px;
    border-radius: 22px;
    overflow: hidden;
  }

  /* Brand mark */
  .brand-mark {
    position: absolute;
    display: flex;
    align-items: center;
    gap: 10px;
  }
  .brand-mark .dot {
    width: 44px; height: 44px; border-radius: 50%;
    background: var(--navy);
    flex-shrink: 0;
  }
  .brand-mark .brand-name {
    font-weight: 800;
    color: var(--blue);
    text-transform: uppercase;
    line-height: 1.1;
  }

  /* Front */
  .card-front {
    background: linear-gradient(160deg, var(--card-white) 0%, #f3f3f3 40%, var(--card-grey) 100%);
  }
  .card-front .brand-mark { top: 30px; right: 30px; }
  .card-front .brand-mark .brand-name { font-size: 14px; width: 150px; }

  .front-content {
    position: absolute;
    left: 34px; right: 34px; top: 0; bottom: 0;
    padding: 0 0 20px;
    display: flex;
    flex-direction: column;
    justify-content: flex-end;
  }
  .person-name {
    font-size: 27px; font-weight: 800; color: var(--navy); line-height: 1.15;
  }
  .person-title {
    display: flex; align-items: center; gap: 8px;
    font-size: 14px; font-weight: 500; color: var(--ink); letter-spacing: 0.5px;
    line-height: 1.3;
  }
  .person-title::after {
    content: ""; width: 70px; height: 1px; background: var(--ink);
  }
  .company { margin-top: 12px; }
  .company-main {
    font-size: 30px; font-weight: 900; color: var(--blue); line-height: 1;
    letter-spacing: 0.5px;
  }
  .company-sub {
    font-size: 13px; font-weight: 800; color: var(--bright-blue); letter-spacing: 0.5px;
    line-height: 1.4;
  }
  .company-tagline {
    font-size: 12.5px; font-weight: 600; color: var(--ink); line-height: 1.4;
  }

  .contacts { list-style: none; margin-top: 10px; }
  .contacts li {
    display: flex; align-items: center; gap: 10px;
    font-size: 16px; color: var(--grey-ink); line-height: 1.4;
  }
  .contacts li + li { margin-top: 5px; }
  .contacts .icon {
    width: 22px; height: 22px; border-radius: 5px;
    background: var(--bright-blue);
    display: flex; align-items: center; justify-content: center;
    flex-shrink: 0;
  }

  /* Back */
  .card-back { background: var(--card-white); }
  .card-back .brand-mark { top: 38px; left: 50%; transform: translateX(-50%); }
  .card-back .brand-mark .dot { width: 58px; height: 58px; }
  .card-back .brand-mark .brand-name { font-size: 19px; width: 220px; }

  .services { position: absolute; top: 128px; left: 0; right: 0; text-align: center; }
  .services-title {
    font-size: 20px; font-weight: 800; color: var(--navy); letter-spacing: 0.5px;
    margin-bottom: 8px;
  }
  .services-list {
    font-size: 13.5px; color: var(--ink); line-height: 1.55; padding: 0 30px;
  }
  .services-list .sep { color: var(--bright-blue); font-size: 16px; margin: 0 4px; }

  .tag-band {
    position: absolute; left: 0; right: 0; bottom: 0; height: 58px;
    background: linear-gradient(90deg, var(--cyan) 0%, var(--blue) 45%, var(--deep-navy) 100%);
    display: flex; align-items: center; justify-content: center;
    color: #fff; font-weight: 800; font-size: 19px; letter-spacing: 1px;
  }
</style>
</head>
<body>

  <section class="card card-front" aria-label="Business card front">
    <div class="brand-mark">
      <span class="dot"></span>
      <span class="brand-name">Steadfast Upkeep Engineering</span>
    </div>

    <div class="front-content">
      <div class="person">
        <p class="person-name">dale Harwick</p>
        <p class="person-title">FOUNDER</p>
      </div>

      <div class="company">
        <p class="company-main">STEADFAST</p>
        <p class="company-sub">UPKEEP ENGINEERING</p>
        <p class="company-tagline">Keeping Your Equipment Running Smoothly</p>
      </div>

      <ul class="contacts">
        <li>
          <span class="icon">
            <svg width="13" height="13" viewBox="0 0 24 24" fill="#fff"><path d="M6.6 10.8a15.1 15.1 0 0 0 6.6 6.6l2.2-2.2a1 1 0 0 1 1-.25 11.4 11.4 0 0 0 3.6.57 1 1 0 0 1 1 1V20a1 1 0 0 1-1 1A17 17 0 0 1 3 4a1 1 0 0 1 1-1h3.5a1 1 0 0 1 1 1 11.4 11.4 0 0 0 .57 3.6 1 1 0 0 1-.25 1z"/></svg>
          </span>
          5073918246
        </li>
        <li>
          <span class="icon">
            <svg width="13" height="13" viewBox="0 0 24 24" fill="#fff"><path d="M2 21l21-9L2 3v7l15 2-15 2z"/></svg>
          </span>
          dale@suevx.com
        </li>
      </ul>
    </div>
  </section>

  <section class="card card-back" aria-label="Business card back">
    <div class="brand-mark">
      <span class="dot"></span>
      <span class="brand-name">Steadfast Upkeep Engineering</span>
    </div>

    <div class="services">
      <p class="services-title">SERVICES OFFERED:</p>
      <p class="services-list">
        Routine Inspections<span class="sep">•</span>Equipment Maintenance<span class="sep">•</span>Emergency Repairs<br>
        Consultation Services<span class="sep">•</span>New installs
      </p>
    </div>

    <div class="tag-band">BE PROACTIVE NOT REACTIVE</div>
  </section>

</body>
</html>
```